Re-design of website: www.veltramedia.ca/en/

Veltrameda B is a promotional agency specializing in on-site marketing. We are re-designing their website.

We have already produced a prototype:
http://norvapixel.com/veltramedia_siteweb/

The architecture in the prototype must be respected. Please dress up the design with green, grey and black circles and other textures found on their current website www.veltramedia.ca

Inspiration for design that we like, clean, flat design:

- http://www.brimfoxlab.co/
- http://quellarworks.com/#!/process
- http://wearetolvane.com/

Delivrables: PSD files of each page of the prototype

Here are the images of their print portfolio: http://ftp.veltramedia.ca/clients/VLM/VELTRAMEDIA-PORTFOLIO-2012_EN.zip

Industry/Entity Type

Architecture

Requirements
Must have
• Responsive Design

```html
<!DOCTYPE html>
<html lang="en">
<head>
<meta charset="utf-8">
<title>Veltrameda B — Agency</title>
<link rel="stylesheet" href="https://fonts.googleapis.com/css2?family=Jost:wght@300;400;500&family=Arimo:wght@400&display=swap">
<style>
:root{
  --green:#acde6e;
  --green-deep:#9fd560;
  --ink:#111111;
  --nav:#1c1c1c;
  --dark:#2f2f2f;
  --disc:#141414;
  --paper:#ffffff;
  --mist:#e9e9e9;
  --rule:#8a8a8a;
  --text:#333333;
}
*{box-sizing:border-box;margin:0;padding:0}
html,body{width:847px;height:1200px;overflow:hidden;background:var(--paper)}
body{position:relative;font-family:"Arimo",Arial,sans-serif;color:var(--ink)}

.site-header{position:absolute;left:0;top:0;width:847px;height:75px;background:var(--paper);display:flex;align-items:center;justify-content:center;gap:10px}
.brand-name{font-family:"Jost",sans-serif;font-weight:500;font-size:28px;letter-spacing:3px;color:var(--ink)}
.brand-dot{width:30px;height:30px;border-radius:50%;background:var(--green)}

.main-nav{position:absolute;left:0;top:75px;width:847px;height:36px;background:var(--nav);display:flex;justify-content:center;align-items:center}
.main-nav a{font-family:"Jost",sans-serif;font-size:13px;color:#fff;text-decoration:none;padding:0 23px;line-height:16px;border-left:1px solid #555}
.main-nav a:first-child{border-left:none}

.hero{position:absolute;left:0;top:111px;width:847px;height:275px;background:linear-gradient(#b2e476,var(--green-deep));text-align:center}
.hero h1{font-family:"Jost",sans-serif;font-weight:400;font-size:48px;line-height:58px;letter-spacing:3px;color:var(--ink);padding-top:45px}

.achievements{position:absolute;left:0;top:386px;width:847px;height:520px;background:linear-gradient(var(--mist),#fff 100px)}
.section-title{position:absolute;left:73px;top:28px;width:701px;display:flex;align-items:center;gap:8px}
.section-title::before,.section-title::after{content:"";flex:1;border-top:3px dotted var(--rule)}
.section-title h2{font-family:"Jost",sans-serif;font-weight:300;font-size:27px;color:var(--ink);white-space:nowrap}

.card{position:absolute;width:330px;height:178px;background:#fff;border:1px solid #dcdcdc;box-shadow:0 1px 3px rgba(0,0,0,.12);padding:5px}
.card-photo{position:relative;height:110px}
.card h3{font-family:"Jost",sans-serif;font-weight:400;font-size:15.5px;margin-top:7px;letter-spacing:.4px}
.card p{font-size:9px;line-height:13px;color:var(--text);margin-top:2px;letter-spacing:.3px}
.zoom{position:absolute;left:128px;top:32px}

.contact-band{position:absolute;left:0;top:906px;width:847px;height:264px;background:var(--dark)}
.feature{position:absolute;top:0;width:200px;text-align:center;color:#fff}
.feature h2{font-family:"Jost",sans-serif;font-weight:300;font-size:23px;margin-top:13px}
.disc{width:124px;height:124px;border-radius:50%;background:var(--disc);border:2px solid #3c3c3c;margin:16px auto 0;display:flex;align-items:center;justify-content:center}
.feature p{font-size:10px;line-height:15.5px;margin-top:16px}

.site-footer{position:absolute;left:0;top:1170px;width:847px;height:30px;background:var(--green);font-size:10px;line-height:30px;padding-left:72px;color:var(--ink)}
</style>
</head>
<body>
<header class="site-header">
  <span class="brand-name">VELTRAMEDA B</span>
  <span class="brand-dot"></span>
</header>

<nav class="main-nav">
  <a href="#">Agency</a><a href="#">Services</a><a href="#">Achievements</a><a href="#">Events</a><a href="#">Careers</a><a href="#">Contact Us</a>
</nav>

<section class="hero">
  <h1>We create beautiful and<br>meaningful design that makes<br>a difference.</h1>
</section>

<section class="achievements">
  <div class="section-title"><h2>Our Achievements 360</h2></div>

  <article class="card" style="left:74px;top:95px">
    <div class="card-photo" role="img" aria-label="City skyline of lit towers at dusk" style="background:linear-gradient(100deg,#6a4aa0,#3b3f7a 40%,#b89a8a 80%,#d9c7b0)"></div>
    <h3>simply dummy text of the printing.</h3>
    <p>simply dummy text of the printing and typesetting industry. Lorem Ipsu m has been the industry's.</p>
  </article>

  <article class="card" style="left:442px;top:95px">
    <div class="card-photo" role="img" aria-label="Person stretching arms upward against a dark teal background" style="background:linear-gradient(90deg,#1d3a42,#2c4d55 50%,#1b3a40)">
      <svg class="zoom" width="52" height="52" viewBox="0 0 52 52" aria-hidden="true">
        <circle cx="21" cy="21" r="16" fill="none" stroke="#fff" stroke-width="5"/>
        <line x1="33" y1="33" x2="47" y2="47" stroke="#fff" stroke-width="7" stroke-linecap="round"/>
        <path d="M21 13v16M13 21h16" stroke="#fff" stroke-width="5"/>
      </svg>
    </div>
    <h3>simply dummy text of the printing.</h3>
    <p>simply dummy text of the printing and typesetting industry. Lorem Ipsu m has been the industry's.</p>
  </article>

  <article class="card" style="left:74px;top:299px">
    <div class="card-photo" role="img" aria-label="Woman relaxing with headphones in a hammock" style="background:linear-gradient(90deg,#3c3033,#6b5048 50%,#8a6a5a)"></div>
    <h3>simply dummy text of the printing.</h3>
    <p>simply dummy text of the printing and typesetting industry. Lorem Ipsu m has been the industry's.</p>
  </article>

  <article class="card" style="left:442px;top:299px">
    <div class="card-photo" role="img" aria-label="Businessman under a black umbrella in a storm" style="background:linear-gradient(180deg,#5a5d60,#8b8e90 60%,#b8b9ba)"></div>
    <h3>simply dummy text of the printing.</h3>
    <p>simply dummy text of the printing and typesetting industry. Lorem Ipsu m has been the industry's.</p>
  </article>
</section>

<section class="contact-band">
  <div class="feature" style="left:58px">
    <h2>Contact Us</h2>
    <div class="disc">
      <svg width="66" height="66" viewBox="0 0 66 66" aria-hidden="true">
        <circle cx="33" cy="33" r="29" fill="none" stroke="var(--green)" stroke-width="5"/>
        <path d="M40 18l6 6-5 5c-2 6-8 12-14 14l-5 5-6-6 6-5 4 2c3-2 6-5 8-8l-2-4z" fill="var(--green)"/>
      </svg>
    </div>
    <p>Lorem ipsum dolor sit amet, consecte-<br>tur adipisicing elit, sed do eiusmod<br>tempor incididunt ut labore.</p>
  </div>
  <div class="feature" style="left:328px">
    <h2>Recrutement</h2>
    <div class="disc">
      <svg width="66" height="66" viewBox="0 0 66 66" aria-hidden="true">
        <circle cx="33" cy="33" r="29" fill="none" stroke="var(--green)" stroke-width="5"/>
        <path d="M19 33l10 10 19-20" fill="none" stroke="var(--green)" stroke-width="7" stroke-linecap="round" stroke-linejoin="round"/>
      </svg>
    </div>
    <p>Lorem ipsum dolor sit amet, consecte-<br>tur adipisicing elit, sed do eiusmod<br>tempor incididunt ut labore.</p>
  </div>
  <div class="feature" style="left:580px">
    <h2>Follow Us</h2>
    <div class="disc">
      <svg width="62" height="62" viewBox="0 0 62 62" aria-hidden="true"><circle cx="31" cy="31" r="30" fill="var(--green)"/></svg>
    </div>
    <p>Lorem ipsum dolor sit amet, consecte-<br>tur adipisicing elit, sed do eiusmod<br>tempor incididunt ut labore.</p>
  </div>
</section>

<footer class="site-footer">(c) Veltrameda B.&nbsp; All rights reserved.</footer>
</body>
</html>
```